Private Investigation Business Card Design

I need a business card for a new private investigation company named Brisk Lens Inquiries. I perform mainly surveillance jobs, vehicle repossessions, document serves etc. The final design should aim for a professional look. The logo has a magnifying glass with stick man arms and legs and is in a running action to show the "BRISK" aspect of the name. If the colour scheme could remain the same as the website www.brisklensinquiries.example.au with silvers,blacks and a couple electric blue highlights.
Industry/Entity Type
Business
Contact Information for Business Card
Morgan Kilbride
Brisk Lens Inquiries
0438276104
PO Box 58, Fernvale NSW 2291
info@brisklensinquiries.example.au
www.brisklensinquiries.example.au
Look and feel
Each slider illustrates characteristics of the customer's brand and the style your logo design should communicate.

```html
<!DOCTYPE html>
<html lang="en">
<head>
<meta charset="utf-8">
<title>Brisk Lens Inquiries – Business Card</title>
<link rel="stylesheet" href="https://fonts.googleapis.com/css2?family=Exo+2:wght@400;700;800&display=swap">
<style>
  :root {
    --backdrop: #efe6d6;
    --card-black: #231f20;
    --card-white: #ffffff;
    --silver: #b9babe;
    --silver-dark: #8e8f94;
    --electric-blue: #4a9ed8;
    --text-light: #f2f2f2;
    --social-1: #3b5b99;
    --social-2: #2a9fd8;
    --social-3: #1d75b0;
    --social-4: #d8372b;
  }
  * { margin: 0; padding: 0; box-sizing: border-box; }
  html, body {
    width: 1189px; height: 1200px; overflow: hidden;
    background: var(--backdrop);
    font-family: "Exo 2", sans-serif;
  }
  .canvas { position: relative; width: 1189px; height: 1200px; }
  .card {
    position: absolute; left: 198px; width: 792px; height: 487px; overflow: hidden;
  }
  .card--front { top: 68px; background: var(--card-black); }
  .card--back { top: 627px; background: var(--card-white); }

  .brand {
    position: absolute; display: flex; align-items: center; gap: 26px;
  }
  .card--front .brand { left: 94px; top: 212px; }
  .card--back .brand { left: 51px; top: 92px; }
  .brand__name {
    font-family: "Exo 2", sans-serif; font-weight: 700; font-size: 40px;
    letter-spacing: 2px; color: var(--silver); white-space: nowrap;
  }
  .card--back .brand__name { color: var(--silver-dark); }
  .brand__mark {
    width: 64px; height: 64px; border-radius: 50%; background: var(--silver);
  }
  .card--back .brand__mark { background: var(--silver-dark); }

  .wave { position: absolute; inset: 0; width: 100%; height: 100%; }

  .contact { position: absolute; left: 51px; top: 278px; color: var(--text-light); }
  .contact__name {
    font-weight: 800; font-size: 33px; letter-spacing: 1.5px; text-transform: uppercase;
    margin-bottom: 12px;
  }
  .contact__list { list-style: none; }
  .contact__item {
    display: flex; align-items: center; gap: 17px; height: 29px;
    font-size: 21px; letter-spacing: 0.6px;
  }
  .contact__icon { width: 20px; height: 20px; flex: none; }
  .contact__address { margin-top: 4px; font-size: 21px; letter-spacing: 0.6px; }

  .social { position: absolute; left: 574px; top: 414px; display: flex; gap: 18px; }
  .social__tile { width: 29px; height: 29px; border-radius: 2px; }
  .social__tile--1 { background: var(--social-1); }
  .social__tile--2 { background: var(--social-2); }
  .social__tile--3 { background: var(--social-3); }
  .social__tile--4 { background: var(--social-4); }
</style>
</head>
<body>
<main class="canvas">

  <section class="card card--front" aria-label="Card front">
    <div class="brand">
      <span class="brand__name">BRISK LENS INQUIRIES</span>
      <span class="brand__mark" aria-hidden="true"></span>
    </div>
  </section>

  <section class="card card--back" aria-label="Card back">
    <div class="brand">
      <span class="brand__name">BRISK LENS INQUIRIES</span>
      <span class="brand__mark" aria-hidden="true"></span>
    </div>

    <svg class="wave" viewBox="0 0 970 597" preserveAspectRatio="none" aria-hidden="true">
      <path fill="var(--electric-blue)"
        d="M0,312 C200,262 450,272 650,318 C800,352 930,300 970,168 L970,330 C800,368 650,348 550,322 C400,287 200,292 0,345 Z"/>
      <path fill="var(--card-black)" stroke="var(--card-white)" stroke-width="7"
        d="M0,350 C200,297 400,292 550,327 C650,352 800,372 975,335 L975,605 L-5,605 Z"/>
    </svg>

    <div class="contact">
      <h1 class="contact__name">Morgan Kilbride</h1>
      <ul class="contact__list">
        <li class="contact__item">
          <svg class="contact__icon" viewBox="0 0 20 20" aria-hidden="true">
            <rect width="20" height="20" fill="#9a9a9a"/>
            <path d="M6 3 L9 6 L7.5 8 Q9 11.5 12 12.5 L14 11 L17 14 L15 17 Q6 15 3 5 Z" fill="#231f20"/>
          </svg>
          <span>0438276104</span>
        </li>
        <li class="contact__item">
          <svg class="contact__icon" viewBox="0 0 20 20" aria-hidden="true">
            <rect width="20" height="20" fill="#9a9a9a"/>
            <rect x="3" y="5" width="14" height="10" fill="none" stroke="#231f20" stroke-width="1.5"/>
            <path d="M3 5 L10 11 L17 5 M3 15 L8 10 M17 15 L12 10" fill="none" stroke="#231f20" stroke-width="1.5"/>
          </svg>
          <span>info@brisklensinquiries.example.au</span>
        </li>
        <li class="contact__item">
          <svg class="contact__icon" viewBox="0 0 20 20" aria-hidden="true">
            <rect width="20" height="20" fill="#9a9a9a"/>
            <circle cx="10" cy="10" r="6.5" fill="none" stroke="#231f20" stroke-width="1.3"/>
            <ellipse cx="10" cy="10" rx="3" ry="6.5" fill="none" stroke="#231f20" stroke-width="1.1"/>
            <path d="M3.5 10 H16.5 M4.5 7 H15.5 M4.5 13 H15.5" stroke="#231f20" stroke-width="1.1"/>
          </svg>
          <span>www.brisklensinquiries.example.au</span>
        </li>
      </ul>
      <p class="contact__address">PO Box 58, Fernvale NSW 2291</p>
    </div>

    <div class="social" aria-label="Social links">
      <span class="social__tile social__tile--1"></span>
      <span class="social__tile social__tile--2"></span>
      <span class="social__tile social__tile--3"></span>
      <span class="social__tile social__tile--4"></span>
    </div>
  </section>

</main>
</body>
</html>
```